Leadership Training Business Needs a business card design

We need a business card designed for our company based in Auckland, New Zealand called Kestrel Pathway Services. We conduct a variety of residential programmes that provide for differnet management levels. These programmes are designed to familiarise managers with important leadership concepts and techniques. This learning is reinforced through the provision of real workplace feedback and the use of action learning opportunities (experiential exercises) to develop the participants' leadership skills and potential. We would like to add our tag line which is:
Inspires Direction - Instils Values - Delivers Results
We would like the card to be a white background but would consider a different background colour on the back. Possibly include the following words on the back:
- Organisational Development
- Positive Cultural Change
- Leadership Programmes
- Practical Development "Tools"
- Crew Guidance Matrix
- 360o degree Assessments
- Strengths Based Training
- Coaching and Mentoring

Must have
• Company Name, logo, contact details, website address and email.
• Persons name and their title

```html
<!DOCTYPE html>
<html lang="en">
<head>
<meta charset="utf-8">
<title>Kestrel Pathway Services – Business Card</title>
<link rel="stylesheet" href="https://fonts.googleapis.com/css2?family=Open+Sans:wght@400;600;700&family=Ubuntu:wght@400;500;700&display=swap">
<style>
  :root {
    --canvas: #ebe8e3;
    --navy: #2e3f97;
    --navy-deep: #26367f;
    --ink: #1d1f24;
    --paper: #ffffff;
    --band: #e2e5ec;
    --mist: #dfe2ee;
    --rule: #c9ccd4;
    --icon: #3a4ba3;
  }
  * { box-sizing: border-box; margin: 0; padding: 0; }
  html, body { width: 1200px; height: 880px; overflow: hidden; }
  body {
    background: var(--canvas);
    position: relative;
    font-family: "Open Sans", Arial, sans-serif;
  }
  .card {
    position: absolute;
    top: 286px;
    width: 540px;
    height: 308px;
    border-radius: 3px;
    box-shadow: 0 6px 18px rgba(0,0,0,0.18);
    overflow: hidden;
  }

  /* ---------- Back ---------- */
  .card-back { left: 40px; background: var(--navy); color: var(--mist); }
  .back-brand {
    position: absolute; left: 34px; top: 62px; width: 230px;
  }
  .brand-dot {
    width: 62px; height: 62px; border-radius: 50%;
    background: var(--mist); opacity: 0.9; margin: 0 0 16px 64px;
  }
  .back-brand .brand-name {
    font-size: 19px; font-weight: 400; color: var(--mist); line-height: 1.15;
  }
  .back-brand .brand-sub {
    font-size: 19px; font-weight: 400; color: var(--mist); line-height: 1.15; padding-left: 2px;
  }
  .services {
    position: absolute; left: 290px; top: 26px; list-style: none;
    font-size: 14px; line-height: 25px; color: var(--mist); font-style: italic;
  }
  .services li::before { content: "• "; }
  .tagline {
    position: absolute; left: 22px; right: 40px; bottom: 14px; height: 34px;
    background: var(--band); color: var(--navy);
    font-weight: 700; font-size: 16.5px;
    display: flex; align-items: center; justify-content: center;
    letter-spacing: 0.1px;
  }

  /* ---------- Front ---------- */
  .card-front { left: 620px; background: var(--paper); font-family: "Ubuntu", Arial, sans-serif; }
  .front-brand { position: absolute; left: 34px; top: 48px; width: 220px; }
  .front-brand .brand-dot {
    width: 56px; height: 56px; margin: 0 0 12px 70px;
    background: #8fbf3a; opacity: 1;
  }
  .front-brand .brand-name { font-size: 17px; color: var(--ink); line-height: 1.15; }
  .front-brand .brand-sub { font-size: 17px; color: var(--navy); line-height: 1.15; }
  .person {
    position: absolute; right: 30px; top: 86px; text-align: right;
  }
  .person-name { font-size: 27px; font-weight: 700; color: var(--navy); line-height: 1; }
  .person-title { font-size: 12px; color: var(--ink); margin-top: 4px; }
  .rule { height: 1px; background: var(--rule); width: 220px; margin: 10px 0 10px auto; }
  .contact { list-style: none; font-size: 13px; color: var(--ink); line-height: 20px; }
  .contact li { display: flex; justify-content: flex-end; align-items: center; gap: 8px; }
  .contact svg { width: 11px; height: 11px; fill: var(--icon); flex: none; }
  .address { display: flex; justify-content: flex-end; align-items: center; gap: 8px;
    font-size: 13px; line-height: 19px; color: var(--ink); }
  .address svg { width: 13px; height: 17px; fill: var(--icon); }
</style>
</head>
<body>

<section class="card card-back" aria-label="Card back">
  <div class="back-brand">
    <div class="brand-dot"></div>
    <div class="brand-name">Kestrel Pathway Services</div>
    <div class="brand-sub">Leadership Programmes</div>
  </div>
  <ul class="services">
    <li>Organisational Development</li>
    <li>Positive Cultural Change</li>
    <li>Leadership Programmes</li>
    <li>Practical Development "Tools"</li>
    <li>Crew Guidance Matrix</li>
    <li>360 Degree Assessments</li>
    <li>Strengths Based Training</li>
    <li>Coaching and Mentoring</li>
  </ul>
  <div class="tagline">Inspires Direction • Instils Values • Delivers Results</div>
</section>

<section class="card card-front" aria-label="Card front">
  <div class="front-brand">
    <div class="brand-dot"></div>
    <div class="brand-name">Kestrel Pathway Services</div>
    <div class="brand-sub">Leadership Programmes</div>
  </div>
  <div class="person">
    <div class="person-name">Name Surname</div>
    <div class="person-title">manager</div>
    <div class="rule"></div>
    <ul class="contact">
      <li>+00 123 45 789
        <svg viewBox="0 0 10 10"><rect x="2" y="0" width="6" height="10" rx="1"/></svg></li>
      <li>+00 123 45 789
        <svg viewBox="0 0 10 10"><rect x="2" y="0" width="6" height="3"/><rect x="0" y="3" width="10" height="4" rx="1"/><rect x="2" y="7" width="6" height="3"/></svg></li>
      <li>office@yourdomain.com
        <svg viewBox="0 0 10 10"><path d="M0 2h10v6H0z M0 2l5 3.5L10 2" /></svg></li>
      <li>www.yourdomain.com
        <svg viewBox="0 0 10 10"><circle cx="5" cy="5" r="5"/><circle cx="5" cy="5" r="3.2" fill="#fff"/><circle cx="5" cy="5" r="1.6"/></svg></li>
    </ul>
    <div class="rule"></div>
    <div class="address">
      <div>Your Address Goes Here<br>City, Country Zipcode</div>
      <svg viewBox="0 0 12 16"><path d="M6 0a6 6 0 0 1 6 6c0 4-6 10-6 10S0 10 0 6a6 6 0 0 1 6-6z"/><circle cx="6" cy="6" r="2.2" fill="#fff"/></svg>
    </div>
  </div>
</section>

</body>
</html>
```